Website Design for a Graphic Design Studio in California

We are working with a graphic design company in California.
PLEASE NOTE: We report and ban any designer that reaches out directly to our customers.

Some sites to use for content/competitors and inspiration:

http://quelvint.co.uk
https://www.fendro.studio
https://www.zuplo.io (Client's Favorite)
https://www.merigoldcrafts.com
https://craftwimble.com
https://www.dravinsultonmask.com/us/home/

Thank you for taking the time to consider designing a website for us. We are web developers based in Stockton, CA, USA. Most of our projects go through the same process. Understanding this process may help you win a project with us. We custom-code all of our websites in-house. We don’t have any requirements as to what tools you use for your design, but we prefer Figma files. For any design that we label as four-stars, we send it to the client for review. The client picks the final design they want us to use. Once we complete this process, we will continue to show additional clients all the four-star sites and purchase them later. Your designs will have multiple chances to sell. For better chances of success, we ask that you follow these guidelines.

IMAGES:
If you use any images or icons in the design, we ask that you have a link to the asset so we can purchase the image/icon. Most of the designs we submit do not have the customer’s images on them unless they have some great images. Be creative; show us the feeling you are trying to portray with your image choices. Use any royalty-free site you choose. We subscribe to Tessaly and mainly use their images, but we can purchase images outside of Tessaly. PLEASE NOTE: we will not submit designs to clients with watermarks on the images.

FONTS:
We ask that you identify the fonts used in the design. This can be done in a message if you want. We typically use Brindle Fonts and Tessaly Fonts.

CONTENT:
We're always open to different content and ideas. We often submit designs with stock images so the client can see our vision. We typically take pictures after the website launch to use their images with our vision. Lorem Ipsum is fine for paragraphs, but we ask that you write the headers in correct English. We want to be able to show the vision and identify the sections of the website.

INSPIRATION:
We typically add a couple of links in the brief of websites we like to help you get started in your design.

REVISIONS:
We do not often ask for revisions of the designs unless we see something in the design that may not appeal to the client. If there are slight changes that we want to make, we do that in the development process.

FEEDBACK:
We rarely give feedback on designs during the design process. We are working on many website projects and do not have the time to provide feedback. We usually respond if your request is well thought out and asks specific questions, but a note asking “feedback, please” usually goes unanswered.

```html
<!DOCTYPE html>
<html lang="en">
<head>
<meta charset="utf-8">
<title>Veltrano Creative</title>
<link rel="stylesheet" href="https://fonts.googleapis.com/css2?family=Marcellus&family=Poppins:wght@300;400;500;600&display=swap">
<style>
:root{
  --gold:#d9a44a;
  --gold-deep:#b98a38;
  --ink:#1d1d1d;
  --grey:#6f6f6f;
  --grey-mid:#8a8a8a;
  --light:#f3f3f3;
  --card:#ececec;
  --dark:#141414;
  --white:#ffffff;
  --serif:'Marcellus', serif;
  --sans:'Poppins', sans-serif;
}
*{margin:0;padding:0;box-sizing:border-box}
html,body{width:1200px;height:4584px;overflow:hidden;background:var(--white);font-family:var(--sans);color:var(--ink)}
.page{position:relative;width:1200px;height:4584px}
.abs{position:absolute}
.btn{position:absolute;display:flex;align-items:center;justify-content:center;font-family:var(--sans);font-weight:600;font-size:10px;letter-spacing:.5px;text-transform:uppercase}
.btn-gold{background:var(--gold);color:var(--ink)}
.btn-white{background:var(--white);color:var(--ink)}
.photo{position:absolute}
.serif{font-family:var(--serif);font-weight:400}
.chev{display:inline-block;vertical-align:middle}

/* nav */
.brand{position:absolute;display:flex;align-items:center;gap:8px}
.brand-dot{width:30px;height:30px;border-radius:50%;border:3px solid var(--gold)}
.brand-name{font-family:var(--serif);color:var(--gold);line-height:1}
.nav-link{position:absolute;top:20px;font-size:10px;text-transform:uppercase;color:var(--ink)}
.nav-link.is-active{color:var(--gold)}

/* hero */
.hero{left:37px;top:53px;width:1126px;height:636px;background:linear-gradient(90deg,#0d0c0b 0%,#1d1916 40%,#4a3a2c 65%,#2c2622 100%)}
.hero-welcome{left:112px;top:250px;font-size:22px;color:var(--gold)}
.hero-title{left:108px;top:280px;font-size:64px;line-height:72px;color:var(--white);letter-spacing:2px}
.hero-tag{left:108px;top:426px;font-size:21px;color:var(--gold);letter-spacing:.5px}

/* about */
.about-frame{left:44px;top:739px;width:22px;height:382px;background:var(--gold)}
.about-frame-top{left:44px;top:739px;width:480px;height:14px;background:var(--gold)}
.about-frame-bottom{left:44px;top:1107px;width:480px;height:14px;background:var(--gold)}
.about-photo{left:59px;top:751px;width:532px;height:358px;background:linear-gradient(180deg,#3a3a3a 0%,#555 55%,#e2e2e2 70%,#f2f2f2 100%)}
.eyebrow{font-size:13px;color:var(--gold);display:flex;align-items:center;gap:8px}
.eyebrow::after{content:"";width:44px;height:1px;background:var(--gold)}
.section-h{font-family:var(--serif);font-size:34px;line-height:44px;color:var(--ink);letter-spacing:1px}
.body-copy{font-size:11px;line-height:17.5px;color:#555}

/* capabilities */
.cap{left:37px;top:1171px;width:1126px;height:538px;background:var(--grey)}
.cap-title{left:93px;top:1236px;font-size:32px;color:var(--white);letter-spacing:1px}
.cap-item{position:absolute;left:89px;width:251px;height:36px;display:flex;align-items:center;gap:16px;padding-left:6px;color:var(--white);font-size:17px;border-bottom:1px solid #8c8c8c}
.cap-item.is-active{background:var(--gold);border-bottom:none}

/* process */
.process{left:0;top:1759px;width:1200px;height:511px;background:var(--light)}
.centered-title{position:absolute;left:0;width:1200px;text-align:center;font-family:var(--serif);font-size:32px;letter-spacing:1px;color:var(--ink)}
.tab{position:absolute;top:1868px;width:182px;height:35px;display:flex;align-items:center;justify-content:center;gap:8px;font-size:17px;color:var(--white);background:var(--grey)}
.tab.is-active{background:var(--gold)}
.step-icon{position:absolute;left:125px;width:70px;height:70px;border-radius:50%;background:var(--grey);display:flex;align-items:center;justify-content:center}
.step-icon span{width:44px;height:44px;border-radius:50%;border:2px solid var(--white)}
.step-title{position:absolute;left:207px;font-size:19px;color:var(--ink)}
.step-text{position:absolute;left:207px;width:240px;font-size:10.5px;line-height:17px;color:#666}
.process-mark{left:492px;top:1977px;width:190px;height:190px;border-radius:50%;border:18px solid var(--grey);display:flex;align-items:center;justify-content:center;font-family:var(--serif);font-size:24px;color:var(--gold)}

/* projects */
.projects{left:0;top:2270px;width:1200px;height:1344px;background:var(--gold)}
.proj-photo{position:absolute;left:37px;width:579px;height:356px;border-right:5px solid #2a2a2a}
.proj-num{position:absolute;left:735px;font-family:var(--sans);font-weight:300;font-size:88px;line-height:1;color:#b58a3d}
.proj-h{position:absolute;left:737px;font-size:32px;color:var(--ink);display:flex;align-items:center;gap:12px}
.proj-text{position:absolute;left:739px;width:405px;font-size:10.5px;line-height:17.5px;color:#2b2b2b}
.divider{position:absolute;left:37px;width:1124px;height:1px;background:#c18f3d}

/* pricing */
.plan{position:absolute;top:3718px;width:351px;height:297px;background:var(--card)}
.plan-head{height:46px;display:flex;align-items:center;justify-content:center;font-weight:600;font-size:19px;color:var(--white);background:var(--grey-mid)}
.plan-head.is-popular{background:var(--gold)}
.plan-head.is-dark{background:var(--dark)}
.badge{position:absolute;left:135px;top:82px;width:82px;height:82px;border-radius:50%;background:var(--white);border:3px solid #d6d6d6;display:flex;flex-direction:column;align-items:center;justify-content:center;color:var(--gold)}
.badge.is-dark{background:#555;border-color:#777;color:var(--white)}
.badge b{font-weight:400;font-size:26px;line-height:1}
.badge small{font-size:8px}
.price{position:absolute;left:0;width:351px;text-align:center;top:180px;font-size:38px;color:var(--ink)}
.timeline{position:absolute;left:0;width:351px;text-align:center;top:233px;font-size:17px;color:var(--ink)}

/* cta */
.cta{left:0;top:4081px;width:1200px;height:270px;background:linear-gradient(180deg,#555 0%,#3f3f3f 100%)}
.cta-left{left:0;top:4081px;width:300px;height:270px;background:radial-gradient(ellipse at 40% 60%,#6a6a6a 0%,#3e3e3e 70%)}
.cta-right{left:900px;top:4081px;width:300px;height:270px;background:radial-gradient(ellipse at 70% 45%,#e9e9e9 0%,#8a8a8a 40%,#3e3e3e 75%)}

/* footer */
.footer{left:0;top:4351px;width:1200px;height:233px;background:var(--dark)}
.foot-rule{position:absolute;top:4389px;width:1px;height:169px;background:#555}
.foot-h{position:absolute;top:4392px;font-family:var(--serif);font-size:16px;color:var(--white);letter-spacing:1px}
.foot-link{position:absolute;left:440px;font-size:8.5px;color:#cfcfcf}
.foot-item{position:absolute;display:flex;align-items:center;gap:10px;font-size:8.5px;color:#cfcfcf;line-height:13px}
.foot-ico{width:16px;height:16px;border-radius:50%;background:var(--gold);flex:none;display:flex;align-items:center;justify-content:center}
</style>
</head>
<body>
<div class="page">

  <!-- navigation -->
  <div class="brand" style="left:39px;top:8px">
    <span class="brand-dot"></span>
    <span class="brand-name"><span style="font-size:21px">VELTRANO</span><br><span style="font-size:12px">CREATIVE</span></span>
  </div>
  <a class="nav-link is-active" style="left:288px">Home</a>
  <a class="nav-link" style="left:372px">About Us</a>
  <a class="nav-link" style="left:480px">Our Capabilities</a>
  <a class="nav-link" style="left:627px">Our Process</a>
  <a class="nav-link" style="left:757px">Project</a>
  <a class="nav-link" style="left:856px">Pricing Plan</a>
  <a class="btn btn-gold" style="left:1054px;top:12px;width:109px;height:29px">Contact Us</a>

  <!-- hero -->
  <div class="abs hero photo" role="img" aria-label="Design team gathered around a studio table reviewing work"></div>
  <div class="abs hero-welcome">Welcome to</div>
  <h1 class="abs hero-title serif">VELTRANO<br>CREATIVE</h1>
  <div class="abs hero-tag">Designing your tomorrow, today.</div>
  <a class="btn btn-gold" style="left:112px;top:477px;width:123px;height:38px">Discover Now</a>

  <!-- about -->
  <div class="abs about-frame"></div>
  <div class="abs about-frame-top"></div>
  <div class="abs about-frame-bottom"></div>
  <div class="abs about-photo photo" role="img" aria-label="Studio reception with branded wall, lounge chairs and plants"></div>
  <div class="abs eyebrow" style="left:721px;top:771px">About Us</div>
  <h2 class="abs section-h" style="left:719px;top:798px">ABOUT
    <svg class="chev" width="34" height="24" viewBox="0 0 34 24"><path d="M2 2l14 10L2 22zM16 2l14 10-14 10z" fill="var(--gold)"/></svg><br>VELTRANO CREATIVE</h2>
  <p class="abs body-copy" style="left:724px;top:897px;width:405px">As a full-service branding and package design agency. We are experts at increasing the value of your brand with imagination, ingenuity and Passion. We know that for your business to thrive, all aspects of your Branding &amp; marketing need to work together. That's why our proven Process Builds from the researchphase to final Asset delivery. Our Team makes sure that everything we create for youspeaks Directly to your ideal customer &amp; helps supportyour business goals.</p>
  <a class="btn btn-gold" style="left:725px;top:1043px;width:128px;height:34px">Read More</a>

  <!-- capabilities -->
  <div class="abs cap"></div>
  <h2 class="abs cap-title serif">OUR CAPABILITIES</h2>
  <div class="cap-item" style="top:1301px"><svg width="20" height="12" viewBox="0 0 20 12"><path d="M1 1l8 5-8 5zM10 1l8 5-8 5z" fill="var(--gold)"/></svg>Branding &amp; Strategy</div>
  <div class="cap-item" style="top:1355px"><svg width="20" height="12" viewBox="0 0 20 12"><path d="M1 1l8 5-8 5zM10 1l8 5-8 5z" fill="var(--gold)"/></svg>Marketing Collateral</div>
  <div class="cap-item" style="top:1408px"><svg width="20" height="12" viewBox="0 0 20 12"><path d="M1 1l8 5-8 5zM10 1l8 5-8 5z" fill="var(--gold)"/></svg>Packaging</div>
  <div class="cap-item" style="top:1460px"><svg width="20" height="12" viewBox="0 0 20 12"><path d="M1 1l8 5-8 5zM10 1l8 5-8 5z" fill="var(--gold)"/></svg>Style Guides</div>
  <div class="cap-item" style="top:1517px;border-bottom:none"><svg width="20" height="12" viewBox="0 0 20 12"><path d="M1 1l8 5-8 5zM10 1l8 5-8 5z" fill="var(--gold)"/></svg>Illustration</div>
  <div class="cap-item is-active" style="top:1561px"><svg width="20" height="12" viewBox="0 0 20 12"><path d="M1 1l8 5-8 5zM10 1l8 5-8 5z" fill="var(--white)"/></svg>Logo Design</div>
  <div class="photo" style="left:514px;top:1189px;width:631px;height:287px;background:linear-gradient(135deg,#2a241e 0%,#6e5a44 45%,#d9d4cc 75%,#3a342e 100%)" role="img" aria-label="Hand sketching a logo on paper beside a keyboard"></div>
  <div class="photo" style="left:514px;top:1494px;width:307px;height:192px;background:linear-gradient(135deg,#c9c3bb 0%,#8c8680 50%,#e5e0d9 100%)" role="img" aria-label="Designer working with software on a monitor and colour wheel"></div>
  <div class="photo" style="left:838px;top:1494px;width:307px;height:192px;background:linear-gradient(135deg,#f1ede6 0%,#d8b88a 45%,#c98a8a 70%,#e7e3dc 100%)" role="img" aria-label="Colour swatches and brand sketches on a desk"></div>

  <!-- process -->
  <div class="abs process"></div>
  <h2 class="centered-title" style="top:1803px">OUR PROCESS</h2>
  <div class="tab is-active" style="left:308px"><svg width="20" height="12" viewBox="0 0 20 12"><path d="M1 1l8 5-8 5zM10 1l8 5-8 5z" fill="var(--white)"/></svg>Discover</div>
  <div class="tab" style="left:507px"><svg width="20" height="12" viewBox="0 0 20 12"><path d="M1 1l8 5-8 5zM10 1l8 5-8 5z" fill="var(--white)"/></svg>Develop</div>
  <div class="tab" style="left:709px"><svg width="20" height="12" viewBox="0 0 20 12"><path d="M1 1l8 5-8 5zM10 1l8 5-8 5z" fill="var(--white)"/></svg>Deliver</div>

  <div class="step-icon" style="top:1943px"><span></span></div>
  <div class="step-title" style="top:1948px">launch Project</div>
  <p class="step-text" style="top:1976px">Lorem ipsum dolor sit amet, consectetur adipiscing elit. Aenean at ante leo.</p>
  <div class="step-icon" style="top:2046px"><span></span></div>
  <div class="step-title" style="top:2051px">Determine Goal</div>
  <p class="step-text" style="top:2079px">Lorem ipsum dolor sit amet, consectetur adipiscing elit. Aenean at ante leo.</p>
  <div class="step-icon" style="top:2150px"><span></span></div>
  <div class="step-title" style="top:2153px">Formulate Plan</div>
  <p class="step-text" style="top:2181px">Lorem ipsum dolor sit amet, consectetur adipiscing elit. Aenean at ante leo.</p>

  <div class="abs process-mark">Veltrano</div>

  <h3 class="abs" style="left:726px;top:1950px;font-weight:400;font-size:29px">DISCOVER</h3>
  <p class="abs body-copy" style="left:727px;top:1996px;width:355px;font-size:10.5px">Deepdive session into project needs and goals<br>Lorem ipsum dolor sit amet, consectetur adipiscing elit. Aenean at ante leo. Nulla ac sodales nulla. Curabitur nec ex urna. Suspendisse ac interdum ligula. In sit amet nibh elit. Duis in leo congue, ultricies libero ac, ultricies augue. Fusce fermentum est justo, in ornare velit placerat pharetra.<br><br>Lorem ipsum dolor sit amet, consectetur adipiscing elit. Aenean at ante leo. Nulla ac sodales nulla. Curabitur nec ex urna. Suspendisse ac interdum ligula. In sit amet nibh elit. Duis in leo congue, ultricies libero ac, ultricies augue. Fusce fermentum est justo, in ornare velit placerat pharetra.</p>

  <!-- projects -->
  <div class="abs projects"></div>
  <h2 class="centered-title" style="top:2335px">OUR PROJECT</h2>

  <div class="proj-photo" style="top:2411px;background:linear-gradient(135deg,#3b3b3b 0%,#9aa0a6 40%,#e8e6e1 70%,#c9b79a 100%)" role="img" aria-label="Desktop computer with design software, pencils and plants"></div>
  <div class="proj-num" style="top:2428px">01</div>
  <div class="proj-h" style="top:2512px">DISCOVER <svg width="36" height="24" viewBox="0 0 36 24"><path d="M2 2l15 10L2 22zM17 2l15 10-15 10z" fill="var(--ink)"/></svg></div>
  <p class="proj-text" style="top:2560px">As a full-service branding and package design agency. We are experts at increasing the value of your brand with imagination, ingenuity and Passion. We know that for your business to thrive, all aspects of your Branding &amp; marketing need to work together. That's why our proven Process Builds from the researchphase to final Asset delivery. Our Team makes sure that everything we create for youspeaks Directly to your ideal customer &amp; helps supportyour business goals.</p>
  <a class="btn btn-white" style="left:739px;top:2708px;width:215px;height:36px">View All Discover Project</a>
  <div class="divider" style="top:2785px"></div>

  <div class="proj-photo" style="top:2806px;background:linear-gradient(135deg,#6a4a30 0%,#b9b3aa 40%,#d9d4cc 60%,#5a3c2a 100%)" role="img" aria-label="Designer sketching a logo at a wooden desk with a computer"></div>
  <div class="proj-num" style="top:2822px">02</div>
  <div class="proj-h" style="top:2906px">DEVELOP <svg width="36" height="24" viewBox="0 0 36 24"><path d="M2 2l15 10L2 22zM17 2l15 10-15 10z" fill="var(--ink)"/></svg></div>
  <p class="proj-text" style="top:2954px">As a full-service branding and package design agency. We are experts at increasing the value of your brand with imagination, ingenuity and Passion. We know that for your business to thrive, all aspects of your Branding &amp; marketing need to work together. That's why our proven Process Builds from the researchphase to final Asset delivery. Our Team makes sure that everything we create for youspeaks Directly to your ideal customer &amp; helps supportyour business goals.</p>
  <a class="btn btn-white" style="left:739px;top:3104px;width:215px;height:36px">View All Develop Project</a>
  <div class="divider" style="top:3183px"></div>

  <div class="proj-photo" style="top:3205px;background:linear-gradient(135deg,#5b8a7a 0%,#d8d6cf 35%,#f2efe8 60%,#c9c5bd 100%)" role="img" aria-label="Collage of typography and interface elements for a design theme"></div>
  <div class="proj-num" style="top:3222px">03</div>
  <div class="proj-h" style="top:3306px">DELIVER <svg width="36" height="24" viewBox="0 0 36 24"><path d="M2 2l15 10L2 22zM17 2l15 10-15 10z" fill="var(--ink)"/></svg></div>
  <p class="proj-text" style="top:3353px">As a full-service branding and package design agency. We are experts at increasing the value of your brand with imagination, ingenuity and Passion. We know that for your business to thrive, all aspects of your Branding &amp; marketing need to work together. That's why our proven Process Builds from the researchphase to final Asset delivery. Our Team makes sure that everything we create for youspeaks Directly to your ideal customer &amp; helps supportyour business goals.</p>
  <a class="btn btn-white" style="left:739px;top:3504px;width:215px;height:36px">View All Deliver Project</a>

  <!-- pricing -->
  <h2 class="centered-title" style="top:3655px">PRICING &amp; PLANS</h2>
  <div class="plan" style="left:37px">
    <div class="plan-head">BRAND BASICS</div>
    <div class="badge"><b>45%</b><small>SAVINGS!</small></div>
    <div class="price">$995</div>
    <div class="timeline">Timeline 3 Weeks</div>
    <a class="btn btn-gold" style="left:113px;top:279px;width:126px;height:34px">View Plans</a>
  </div>
  <div class="plan" style="left:424px">
    <div class="plan-head is-popular">MOST POPULAR! BRAND PRO</div>
    <div class="badge is-dark" style="top:76px;width:94px;height:94px;left:129px"><b>55%</b><small>SAVINGS!</small></div>
    <div class="price" style="top:186px">$2495</div>
    <div class="timeline" style="top:239px">Timeline 4 Weeks</div>
    <a class="btn btn-gold" style="left:113px;top:279px;width:126px;height:34px">View Plans</a>
  </div>
  <div class="plan" style="left:808px">
    <div class="plan-head is-dark">BRAND PREMIUM</div>
    <div class="badge"><b>50%</b><small>SAVINGS!</small></div>
    <div class="price">$3498</div>
    <div class="timeline">Timeline 6 Weeks</div>
    <a class="btn btn-gold" style="left:113px;top:279px;width:126px;height:34px">View Plans</a>
  </div>

  <!-- call to action -->
  <div class="abs cta"></div>
  <div class="abs cta-left photo" role="img" aria-label="Glasses, plant and coffee cup on a dark desk"></div>
  <div class="abs cta-right photo" role="img" aria-label="Laptop, notebook and plants on a dark desk"></div>
  <div class="abs" style="left:560px;top:4118px;width:80px;height:80px;border-radius:50%;border:9px solid var(--white)"></div>
  <div class="abs serif" style="left:0;width:1200px;text-align:center;top:4218px;font-size:34px;color:var(--white);letter-spacing:1px">LET'S WORK TOGETHER</div>
  <a class="btn btn-gold" style="left:538px;top:4280px;width:126px;height:32px">Get Started</a>

  <!-- footer -->
  <div class="abs footer"></div>
  <div class="brand" style="left:39px;top:4400px">
    <span class="brand-dot" style="width:40px;height:40px"></span>
    <span class="brand-name"><span style="font-size:26px">VELTRANO</span><br><span style="font-size:15px">CREATIVE</span></span>
  </div>
  <div class="abs" style="left:53px;top:4468px;font-size:8px;color:#bdbdbd">© 2023 VELTRANO CREATIVE. All rights reserved</div>

  <div class="foot-rule" style="left:336px"></div>
  <div class="foot-rule" style="left:625px"></div>
  <div class="foot-rule" style="left:937px"></div>

  <div class="foot-h" style="left:442px">ABOUT US</div>
  <div class="foot-link" style="top:4428px">Home</div>
  <div class="foot-link" style="top:4446px">About Us</div>
  <div class="foot-link" style="top:4464px">Our Capabilities</div>
  <div class="foot-link" style="top:4482px">Our Process</div>
  <div class="foot-link" style="top:4500px">Project</div>
  <div class="foot-link" style="top:4518px">Pricing plan</div>
  <div class="foot-link" style="top:4536px">Contact Us</div>

  <div class="foot-h" style="left:703px">CONTACT US</div>
  <div class="foot-item" style="left:703px;top:4424px"><span class="foot-ico"><svg width="8" height="10" viewBox="0 0 8 10"><path d="M4 0a4 4 0 0 0-4 4c0 3 4 6 4 6s4-3 4-6a4 4 0 0 0-4-4z" fill="var(--dark)"/></svg></span>2140 Marlow Ave Suite B<br>Fernvale, CA 90000</div>
  <div class="foot-item" style="left:703px;top:4458px"><span class="foot-ico"><svg width="10" height="8" viewBox="0 0 10 8"><rect x="0" y="0" width="10" height="8" fill="var(--dark)"/><path d="M0 0l5 4 5-4" stroke="var(--gold)" fill="none"/></svg></span>hello@veltranocreative.com</div>
  <div class="foot-item" style="left:703px;top:4487px"><span class="foot-ico"><svg width="8" height="8" viewBox="0 0 8 8"><circle cx="4" cy="4" r="3" fill="none" stroke="var(--dark)" stroke-width="1.4"/></svg></span>veltranocreative.com</div>
  <div class="foot-item" style="left:703px;top:4516px"><span class="foot-ico"><svg width="8" height="8" viewBox="0 0 8 8"><path d="M1 1c0 3 3 6 6 6l1-2-2-1-1 1C4 5 3 4 2 3l1-1-1-2z" fill="var(--dark)"/></svg></span>555.014.2290</div>

  <div class="foot-h" style="left:1040px">FOLLOW US</div>
  <div class="foot-item" style="left:1040px;top:4428px"><span class="foot-ico"></span>Pagecircle</div>
  <div class="foot-item" style="left:1040px;top:4458px"><span class="foot-ico"></span>Framelane</div>
  <div class="foot-item" style="left:1040px;top:4488px"><span class="foot-ico"></span>Chirpline</div>

</div>
</body>
</html>
```